Christmas Card Design

We are in need of a Christmas card design to send to other doctors this year. Uploaded files include our card from last year and our "RT" logo. Our goal is to incorporate our "RT" logo in whatever design we have. Last year, we used it as Christmas ornaments on a tree. The front of the card would also need to read "Happy Holidays". It could have a Santa, reindeer, snowman, or whatever ideas you have to give it the holiday feel.

```html
<!DOCTYPE html>
<html lang="en">
<head>
<meta charset="utf-8">
<title>Happy Holidays – Rivertown Oncology</title>
<link href="https://fonts.googleapis.com/css2?family=Montserrat:wght@400;500;700&display=swap" rel="stylesheet">
<style>
  :root {
    --paper: #ffffff;
    --ice: #b8e3e8;
    --ice-soft: #d6eff2;
    --ice-faint: #e6f5f7;
    --greeting: #86d2da;
    --brand-red: #e5332a;
    --brand-navy: #2d5c7c;
  }
  html, body {
    margin: 0;
    padding: 0;
    overflow: hidden;
    background: var(--paper);
  }
  .card {
    position: relative;
    width: 1200px;
    height: 927px;
    overflow: hidden;
    background: var(--paper);
    font-family: "Montserrat", sans-serif;
  }
  .snowflake {
    position: absolute;
    border-radius: 50%;
  }
  .snowflake--small {
    left: 300px; top: 76px; width: 200px; height: 200px;
    background: radial-gradient(circle, var(--ice) 0%, var(--ice) 40%, rgba(184,227,232,0) 72%);
  }
  .snowflake--left {
    left: -68px; top: 148px; width: 384px; height: 384px;
    background: radial-gradient(circle, var(--ice) 0%, var(--ice) 42%, rgba(184,227,232,0) 72%);
  }
  .snowflake--top-right {
    left: 772px; top: -156px; width: 592px; height: 592px;
    background: radial-gradient(circle, var(--ice) 0%, var(--ice) 44%, rgba(184,227,232,0) 72%);
  }
  .snowflake--bottom {
    left: 472px; top: 556px; width: 464px; height: 464px;
    background: radial-gradient(circle, var(--ice-soft) 0%, var(--ice-soft) 42%, rgba(214,239,242,0) 72%);
  }
  .snowflake--bottom-right {
    left: 936px; top: 680px; width: 304px; height: 304px;
    background: radial-gradient(circle, var(--ice-faint) 0%, var(--ice-faint) 40%, rgba(230,245,247,0) 72%);
  }
  .greeting {
    position: absolute;
    left: 700px;
    top: 390px;
    width: 404px;
    text-align: center;
  }
  .greeting__dot {
    display: block;
    width: 84px;
    height: 84px;
    margin: 0 auto 14px;
    border-radius: 50%;
    background: var(--brand-red);
  }
  .greeting__text {
    margin: 0;
    font-size: 40px;
    font-weight: 500;
    color: var(--greeting);
    line-height: 1;
  }
  .signoff {
    position: absolute;
    left: 60px;
    top: 760px;
  }
  .signoff__brand {
    display: flex;
    align-items: center;
  }
  .signoff__dot {
    width: 64px;
    height: 64px;
    border-radius: 50%;
    background: var(--brand-red);
    margin-right: 14px;
    flex: none;
  }
  .signoff__names {
    display: flex;
    flex-direction: column;
    align-items: flex-end;
  }
  .signoff__name {
    font-size: 36px;
    font-weight: 400;
    color: var(--brand-navy);
    line-height: 1;
  }
  .signoff__tagline {
    font-size: 18px;
    font-weight: 400;
    color: var(--brand-navy);
    margin-top: 4px;
  }
  .signoff__web {
    display: block;
    margin: 14px 0 0 6px;
    font-size: 27px;
    font-weight: 700;
    color: var(--brand-red);
    text-decoration: none;
    letter-spacing: 0.3px;
  }
</style>
</head>
<body>
  <main class="card">
    <div class="snowflake snowflake--small" role="img" aria-label="Small ornate paper-cut snowflake in pale ice blue"></div>
    <div class="snowflake snowflake--left" role="img" aria-label="Large ornate paper-cut snowflake in pale ice blue"></div>
    <div class="snowflake snowflake--top-right" role="img" aria-label="Large ornate paper-cut snowflake in pale ice blue, cropped at the corner"></div>
    <div class="snowflake snowflake--bottom" role="img" aria-label="Faded ornate paper-cut snowflake in very pale blue"></div>
    <div class="snowflake snowflake--bottom-right" role="img" aria-label="Faint ornate paper-cut snowflake, cropped at the corner"></div>

    <section class="greeting">
      <span class="greeting__dot"></span>
      <h1 class="greeting__text">happy holidays</h1>
    </section>

    <footer class="signoff">
      <div class="signoff__brand">
        <span class="signoff__dot"></span>
        <div class="signoff__names">
          <span class="signoff__name">Rivertown Oncology</span>
          <span class="signoff__tagline">Healing Together.</span>
        </div>
      </div>
      <a class="signoff__web" href="#">www.rivertownoncology.com</a>
    </footer>
  </main>
</body>
</html>
```